upmarket Hair salon A5 flyer design colour double sided

Phone number 9318 7061
address is shop 3/7 Marlowe pde Butler
Hi i am wanting a flyer that is upmarket and elegant for my hair salon Velvet Strands For Hair if any pics of hair must look great.
both side must have logo and contact details on
offer side 1
50% off
style cut and finish
*not valid Saturdays
*expires 31/03/15
*butler salon only
*not valid with any other offers
offer side 2
1/2 head foils or all over colour,
cut and finish
$120
*toners and treatment extra costs
*expires 31/03/15
*butler salon only

```html
<!DOCTYPE html>
<html lang="en">
<head>
<meta charset="utf-8">
<title>Velvet Strands For Hair – Salon Offers</title>
<link rel="stylesheet" href="https://fonts.googleapis.com/css2?family=Tinos:ital,wght@0,400;1,400&display=swap">
<style>
  :root {
    --page: #ffffff;
    --ink: #1e1a1a;
    --teal-deep: #00605a;
    --teal: #0e7a73;
    --teal-light: #3a9a9a;
    --band-dark: #231f1f;
    --hair-dark: #15171f;
    --hair-mid: #3a4152;
    --tag-red: #d9282d;
    --tag-red-deep: #b11d24;
    --text-light: #ffffff;
  }
  * { margin: 0; padding: 0; box-sizing: border-box; }
  html, body {
    width: 853px; height: 1200px; overflow: hidden;
    background: var(--page);
  }
  body { position: relative; font-family: "Tinos", "Times New Roman", serif; }

  .flyer {
    position: absolute; left: 22px; width: 808px; height: 568px;
    overflow: hidden; background: var(--page);
  }
  .flyer--discount { top: 24px; }
  .flyer--colour { top: 616px; }

  .flyer__art { position: absolute; inset: 0; width: 100%; height: 100%; }

  .brand {
    position: absolute; right: 38px; top: 46px;
    color: var(--ink); font-weight: 400; font-style: normal;
    line-height: 1; text-align: right;
  }
  .brand__main { display: block; font-size: 40px; letter-spacing: 0.5px; }
  .brand__sub { display: block; font-size: 18px; margin-top: 6px; }

  .offer-tag {
    position: absolute; left: 363px; top: 229px; width: 202px; height: 202px;
    display: flex; flex-direction: column; align-items: center; justify-content: center;
    color: var(--text-light); font-style: italic; text-align: center;
  }
  .offer-tag__headline { font-style: normal; font-size: 52px; line-height: 1; position: relative; }
  .offer-tag__suffix { font-style: italic; font-size: 26px; vertical-align: 18px; }
  .offer-tag__mark { position: absolute; right: 18px; top: -24px; font-size: 24px; font-style: normal; }
  .offer-tag__service { font-size: 27px; line-height: 1.1; margin-top: 8px; }
  .offer-tag__lines { font-size: 21px; line-height: 1.12; }
  .offer-tag__price { font-style: normal; font-size: 44px; line-height: 1; margin-top: 10px; }

  .conditions {
    position: absolute; left: 55px; top: 444px; list-style: none;
    color: var(--text-light); font-style: italic; font-size: 16px; line-height: 22px;
  }
  .conditions li::before { content: "\2217"; font-style: normal; margin-right: 9px; }

  .contact {
    position: absolute; left: 591px; top: 432px;
    color: var(--text-light); font-style: italic;
  }
  .contact__title { font-size: 22px; line-height: 28px; font-weight: 400; }
  .contact__phone { font-size: 12px; line-height: 30px; }
  .contact__phone-number { font-size: 21px; margin-left: 4px; }
  .contact__address { font-size: 12.5px; line-height: 22px; }
</style>
</head>
<body>

<section class="flyer flyer--discount">
  <svg class="flyer__art" viewBox="0 0 941 662" preserveAspectRatio="none">
    <defs>
      <linearGradient id="hairTone1" x1="0" y1="0" x2="1" y2="0.4">
        <stop offset="0" stop-color="var(--hair-mid)"/>
        <stop offset="0.5" stop-color="var(--hair-dark)"/>
        <stop offset="1" stop-color="var(--hair-mid)"/>
      </linearGradient>
      <linearGradient id="tealFade1" x1="0" y1="0" x2="0" y2="1">
        <stop offset="0" stop-color="var(--teal)"/>
        <stop offset="1" stop-color="var(--teal-deep)"/>
      </linearGradient>
      <radialGradient id="tagFill1" cx="0.5" cy="0.35" r="0.7">
        <stop offset="0" stop-color="var(--tag-red)"/>
        <stop offset="1" stop-color="var(--tag-red-deep)"/>
      </radialGradient>
    </defs>
    <path d="M780,0 H941 V48 C900,25 850,10 780,0 Z" fill="var(--band-dark)"/>
    <path role="img" aria-label="Photograph of long, glossy dark hair flowing in a wave across the flyer"
          d="M0,0 H290 C360,20 380,170 440,210 C520,245 700,170 941,120 V460 H0 Z"
          fill="url(#hairTone1)"/>
    <path d="M0,235 C70,300 170,370 320,405 L0,430 Z" fill="var(--band-dark)"/>
    <path d="M0,330 C150,400 300,425 450,405 C620,380 760,280 941,225 V662 H0 Z" fill="url(#tealFade1)"/>
    <path d="M170,372 C300,420 450,410 560,350 C680,290 820,262 941,255 V300 C820,320 700,380 600,420 C460,460 300,440 170,372 Z" fill="var(--teal-light)"/>
    <circle cx="541" cy="385" r="118" fill="url(#tagFill1)"/>
    <circle cx="639" cy="397" r="10" fill="none" stroke="#fff" stroke-width="3"/>
    <path d="M648,400 C700,405 760,410 780,440 C790,460 770,450 700,425 C680,418 660,405 648,400" fill="none" stroke="#111" stroke-width="1.6"/>
  </svg>

  <div class="brand">
    <span class="brand__main">Velvet Strands</span>
    <span class="brand__sub">for hair</span>
  </div>

  <div class="offer-tag">
    <p class="offer-tag__headline">50%<span class="offer-tag__suffix">-off</span><span class="offer-tag__mark">*</span></p>
    <p class="offer-tag__service">style cut &amp;<br>finish</p>
  </div>

  <ul class="conditions">
    <li>Not valid Saturdays</li>
    <li>Expires 31/03/15</li>
    <li>Butler salon only</li>
    <li>Not valid with any other offers</li>
  </ul>

  <div class="contact">
    <h2 class="contact__title">Contact details</h2>
    <p class="contact__phone">Phone <span class="contact__phone-number">9318 7061</span></p>
    <p class="contact__address">Address is shop</p>
    <p class="contact__address">3/7 Marlowe pde Butler</p>
  </div>
</section>

<section class="flyer flyer--colour">
  <svg class="flyer__art" viewBox="0 0 941 662" preserveAspectRatio="none">
    <defs>
      <linearGradient id="hairTone2" x1="0" y1="0" x2="1" y2="0.4">
        <stop offset="0" stop-color="var(--hair-mid)"/>
        <stop offset="0.5" stop-color="var(--hair-dark)"/>
        <stop offset="1" stop-color="var(--hair-mid)"/>
      </linearGradient>
      <linearGradient id="tealFade2" x1="0" y1="0" x2="0" y2="1">
        <stop offset="0" stop-color="var(--teal)"/>
        <stop offset="1" stop-color="var(--teal-deep)"/>
      </linearGradient>
      <radialGradient id="tagFill2" cx="0.5" cy="0.35" r="0.7">
        <stop offset="0" stop-color="var(--tag-red)"/>
        <stop offset="1" stop-color="var(--tag-red-deep)"/>
      </radialGradient>
    </defs>
    <path d="M780,0 H941 V48 C900,25 850,10 780,0 Z" fill="var(--band-dark)"/>
    <path role="img" aria-label="Photograph of long, glossy dark hair flowing in a wave across the flyer"
          d="M0,0 H290 C360,20 380,170 440,210 C520,245 700,170 941,120 V460 H0 Z"
          fill="url(#hairTone2)"/>
    <path d="M0,235 C70,300 170,370 320,405 L0,430 Z" fill="var(--band-dark)"/>
    <path d="M0,330 C150,400 300,425 450,405 C620,380 760,280 941,225 V662 H0 Z" fill="url(#tealFade2)"/>
    <path d="M170,372 C300,420 450,410 560,350 C680,290 820,262 941,255 V300 C820,320 700,380 600,420 C460,460 300,440 170,372 Z" fill="var(--teal-light)"/>
    <circle cx="541" cy="385" r="118" fill="url(#tagFill2)"/>
    <circle cx="639" cy="397" r="10" fill="none" stroke="#fff" stroke-width="3"/>
    <path d="M648,400 C700,405 760,410 780,440 C790,460 770,450 700,425 C680,418 660,405 648,400" fill="none" stroke="#111" stroke-width="1.6"/>
  </svg>

  <div class="brand">
    <span class="brand__main">Velvet Strands</span>
    <span class="brand__sub">for hair</span>
  </div>

  <div class="offer-tag">
    <p class="offer-tag__lines">1/2 Head foils<br>or<br>All over colour,<br>Cut and finish</p>
    <p class="offer-tag__price">$120</p>
  </div>

  <ul class="conditions">
    <li>Toners and treatment extra costs</li>
    <li>Expires 31/03/15</li>
    <li>Butler salon only</li>
    <li>Not valid with any other offers</li>
  </ul>

  <div class="contact">
    <h2 class="contact__title">Contact details</h2>
    <p class="contact__phone">Phone <span class="contact__phone-number">9318 7061</span></p>
    <p class="contact__address">Address is shop</p>
    <p class="contact__address">3/7 Marlowe pde Butler</p>
  </div>
</section>

</body>
</html>
```